business card

Business card for new business.
Red and black corporate colors.
Card can have an Indsutrial feel to it. Feel free to add Rust, Bolted steel, or graphics as you see fit. We provide highly specialized services to the below mentioned industries.
Keep information out of corners so that if I want I can choose rounded corners.
Information
- front. name - title - phone - email
- Rear
Refining - Rail - Infrastructure - Mining - Energy
Calgary - Edmonton - Fort McMurray - Revelstoke - Vancouver

```html
<!DOCTYPE html>
<html lang="en">
<head>
<meta charset="utf-8">
<title>Ironline Business Card</title>
<link rel="stylesheet" href="https://fonts.googleapis.com/css2?family=Roboto:wght@400;700;900&display=swap">
<style>
  :root {
    --page-bg: #2a2a2a;
    --card-bg: #1c1c1d;
    --card-edge: #262628;
    --brand-red: #e3191f;
    --steel-grey: #8a8a8c;
    --text-grey: #9a9a9c;
    --text-light: #b9b9bb;
  }
  * { box-sizing: border-box; margin: 0; padding: 0; }
  html, body {
    width: 1200px; height: 1189px; overflow: hidden;
    background: var(--page-bg);
    font-family: "Roboto", Arial, sans-serif;
  }
  .canvas { position: relative; width: 1200px; height: 1189px; }
  .card {
    position: absolute; left: 140px;
    width: 920px; height: 526px;
    background: linear-gradient(160deg, var(--card-edge), var(--card-bg) 60%);
    border-radius: 28px;
  }
  .card--back { top: 50px; }
  .card--front { top: 613px; }

  .brand {
    display: flex; align-items: center; gap: 14px;
    font-weight: 900; color: var(--steel-grey);
    letter-spacing: 2px; line-height: 1; white-space: nowrap;
  }
  .brand__mark { width: 22px; height: 22px; background: var(--brand-red); flex: none; }

  /* Back side */
  .card--back .brand { position: absolute; left: 300px; top: 170px; font-size: 78px; }
  .card--back .brand__mark { width: 30px; height: 30px; }
  .service-list {
    position: absolute; left: 300px; top: 290px;
    color: var(--text-grey); font-size: 23px; line-height: 1.6;
    white-space: nowrap;
  }
  .service-list .sep { color: var(--brand-red); padding: 0 8px; }

  /* Front side */
  .card--front .brand { position: absolute; left: 90px; top: 228px; font-size: 62px; }
  .divider {
    position: absolute; left: 500px; top: 190px;
    width: 2px; height: 140px; background: var(--brand-red);
  }
  .contact { position: absolute; left: 545px; top: 180px; white-space: nowrap; }
  .contact__name { color: var(--brand-red); font-size: 26px; letter-spacing: 1px; }
  .contact__title { color: var(--text-grey); font-size: 22px; margin-bottom: 24px; }
  .contact__line {
    display: flex; align-items: center; gap: 12px;
    color: var(--text-light); font-size: 22px; line-height: 1.5;
  }
  .contact__icon { width: 20px; height: 20px; flex: none; }
</style>
</head>
<body>
<main class="canvas">

  <section class="card card--back" aria-label="Card back">
    <div class="brand"><span class="brand__mark"></span>IRONLINE</div>
    <div class="service-list">
      <p>Fabrication<span class="sep">|</span>Pipeline<span class="sep">|</span>Structural<span class="sep">|</span>Marine<span class="sep">|</span>Utilities</p>
      <p>Ashvale<span class="sep">|</span>Kellridge<span class="sep">|</span>Port Harlan<span class="sep">|</span>Greystone<span class="sep">|</span>Millbrook</p>
    </div>
  </section>

  <section class="card card--front" aria-label="Card front">
    <div class="brand"><span class="brand__mark"></span>IRONLINE</div>
    <div class="divider"></div>
    <div class="contact">
      <p class="contact__name">JORDAN HALE</p>
      <p class="contact__title">Managing Director</p>
      <p class="contact__line">
        <svg class="contact__icon" viewBox="0 0 20 20" aria-hidden="true">
          <path fill="#e3191f" d="M2 7c0-2 3-4 8-4s8 2 8 4l-3 1-1-2c-2-.6-6-.6-8 0L5 8z"/>
          <rect x="4" y="9" width="12" height="8" rx="2" fill="#e3191f"/>
        </svg>
        (01) 5550 1234
      </p>
      <p class="contact__line">
        <svg class="contact__icon" viewBox="0 0 20 20" aria-hidden="true">
          <rect x="1" y="4" width="18" height="12" fill="#e3191f"/>
          <path d="M1 4l9 7 9-7" fill="none" stroke="#1c1c1d" stroke-width="1.5"/>
        </svg>
        info@ironlinegroup.com
      </p>
    </div>
  </section>

</main>
</body>
</html>
```